my business card

Please think outside the box
I want this card to stand out letting them know that they are talking to the best in the industry and this is the place to buy a hot tub and or swim spa

Target Market(s)

new hot tub buyers. Family

Contact Information for Business Card

Name: Corla Vantressi

Font styles to use
Serif

Colors

Designer to choose colors to be used in the design.

Requirements
Must have
• Vivid colors
• Promote the healing and fun of using hot tubs & Swim Spas
• largest showroom for hot tubs and swim spas
• in the back of the card:
• Notes:________________________________________
• Your Private wet test appointment is on___________________
Nice to have
• picture
• website address: www.bubblebaynook.example
• phone numbers; office:5558173046 cell 5552694781
• my email: corla@bubblebaynook.example
• unique card material like plastic
• Exclusive Bluefern Soaks & Aquatrell Swim Spa Dealer
Should not have
• very small fonts

```html
<!DOCTYPE html>
<html lang="en">
<head>
<meta charset="utf-8">
<title>Bubble Bay Nook – Business Card</title>
<link rel="stylesheet" href="https://fonts.googleapis.com/css2?family=Roboto:wght@400;500&family=Work+Sans:wght@400&display=swap">
<style>
  :root {
    --bg: #e4e2de;
    --card: #ffffff;
    --ink: #1c1c1c;
    --navy: #2a4c8a;
    --charcoal: #2b2d30;
    --water-deep: #1f4550;
    --water-mid: #3d6f7a;
    --water-light: #5e8d96;
    --teal: #2aa595;
    --white: #ffffff;
  }
  * { box-sizing: border-box; margin: 0; padding: 0; }
  html, body { width: 1200px; height: 930px; overflow: hidden; }
  body {
    background: var(--bg);
    font-family: "Roboto", sans-serif;
    position: relative;
  }
  .card {
    position: absolute;
    left: 250px;
    width: 700px;
    height: 400px;
    border-radius: 16px;
    background: var(--card);
    overflow: hidden;
    box-shadow: 0 6px 18px rgba(0,0,0,0.18);
  }
  .card--back { top: 45px; }
  .card--front { top: 485px; }

  .brand {
    position: absolute;
    display: flex;
    align-items: center;
    gap: 10px;
    font-family: "Roboto", sans-serif;
    font-weight: 500;
    color: var(--ink);
    white-space: nowrap;
  }
  .brand__dot {
    border-radius: 50%;
    background: var(--teal);
    flex: none;
  }
  .card--back .brand { top: 70px; right: 70px; font-size: 30px; }
  .card--back .brand__dot { width: 22px; height: 22px; }
  .card--front .brand { top: 90px; left: 40px; font-size: 28px; }
  .card--front .brand__dot { width: 22px; height: 22px; }

  .back-fields {
    position: absolute;
    left: 60px;
    right: 50px;
    top: 185px;
    font-family: "Work Sans", sans-serif;
    font-size: 17px;
    color: var(--ink);
    letter-spacing: 0.5px;
  }
  .field {
    display: flex;
    align-items: flex-end;
    gap: 8px;
    margin-bottom: 60px;
  }
  .field__rule {
    flex: 1;
    border-bottom: 1.5px solid var(--ink);
    height: 1px;
    margin-bottom: 4px;
  }
  .field--appointment { padding-left: 60px; }

  .front-art { position: absolute; inset: 0; }

  .contact {
    position: absolute;
    right: 40px;
    top: 110px;
    text-align: right;
    color: var(--white);
    white-space: nowrap;
  }
  .contact__name {
    font-size: 28px;
    font-weight: 500;
    letter-spacing: 0.3px;
    text-transform: uppercase;
    line-height: 33px;
  }
  .contact__role {
    font-size: 16px;
    margin-top: 2px;
    margin-bottom: 18px;
  }
  .contact__line {
    display: flex;
    justify-content: flex-end;
    align-items: center;
    gap: 10px;
    font-size: 17px;
    line-height: 26px;
  }
  .contact__icon { width: 14px; height: 14px; flex: none; }
</style>
</head>
<body>

<section class="card card--back">
  <div class="brand"><span class="brand__dot"></span>Bubble Bay Nook</div>
  <div class="back-fields">
    <div class="field"><span>Notes:</span><span class="field__rule"></span></div>
    <div class="field field--appointment"><span>Your Private wet test appointment is on</span><span class="field__rule"></span></div>
  </div>
</section>

<section class="card card--front">
  <svg class="front-art" viewBox="0 0 700 400" width="700" height="400">
    <defs>
      <linearGradient id="waterTone" x1="0" y1="0" x2="1" y2="1">
        <stop offset="0" stop-color="var(--water-light)"/>
        <stop offset="0.5" stop-color="var(--water-mid)"/>
        <stop offset="1" stop-color="var(--water-deep)"/>
      </linearGradient>
    </defs>
    <g transform="translate(-40,0)">
      <path d="M-10,334 C200,334 270,304 312,204 C350,104 400,54 760,54 L760,400 L-10,400 Z"
            fill="var(--charcoal)"/>
      <path d="M-10,352 C200,352 270,322 312,222 C350,122 400,72 760,72 L760,400 L-10,400 Z"
            fill="url(#waterTone)" role="img" aria-label="Photo of a swimmer in a blue swim spa"/>
      <path d="M-10,326 C200,326 270,296 312,196 C350,96 400,46 760,46"
            fill="none" stroke="var(--navy)" stroke-width="9"/>
      <path d="M-10,340 C200,340 270,310 312,210 C350,110 400,60 760,60"
            fill="none" stroke="var(--white)" stroke-width="5"/>
    </g>
  </svg>

  <div class="brand"><span class="brand__dot"></span>Bubble Bay Nook</div>

  <div class="contact">
    <div class="contact__name">Corla Vantressi</div>
    <div class="contact__role">Director</div>
    <div class="contact__line">5558173046
      <svg class="contact__icon" viewBox="0 0 16 16"><path d="M4 1l3 3-2 2c1 2 3 4 5 5l2-2 3 3-2 3C7 15 1 9 1 3z" fill="none" stroke="#fff" stroke-width="1.3"/></svg>
    </div>
    <div class="contact__line">5552694781
      <svg class="contact__icon" viewBox="0 0 16 16"><rect x="4" y="1" width="8" height="14" rx="1.5" fill="none" stroke="#fff" stroke-width="1.3"/><circle cx="8" cy="12.5" r="0.9" fill="#fff"/></svg>
    </div>
    <div class="contact__line">corla@bubblebaynook.example
      <svg class="contact__icon" viewBox="0 0 16 16"><rect x="1" y="3" width="14" height="10" rx="1" fill="none" stroke="#fff" stroke-width="1.3"/><path d="M1 4l7 5 7-5" fill="none" stroke="#fff" stroke-width="1.3"/></svg>
    </div>
    <div class="contact__line">www.bubblebaynook.example
      <svg class="contact__icon" viewBox="0 0 16 16"><circle cx="8" cy="8" r="6.5" fill="none" stroke="#fff" stroke-width="1.3"/><path d="M1.5 8h13M8 1.5c-3 3.5-3 9.5 0 13M8 1.5c3 3.5 3 9.5 0 13" fill="none" stroke="#fff" stroke-width="1.1"/></svg>
    </div>
  </div>
</section>

</body>
</html>
```